Bluebird Business Card Design

Name Marlene Obadofor
Title Mortgage Originator
Office (800) 416-2795 x65
Direct (240) 615-2079
Email mobadofor@bluebirdlending.example
NMLS 3817465
Licensed MD

Name Dorian Pelletier
Title Mortgage Originator
Office (800) 416-2795 x66
Direct (404) 263-5147
Email dpelletier@bluebirdlending.example
NMLS 3156702
Licensed MD

Name Rochelle Barnaby
Title Mortgage Originator
Office (800) 416-2795 x67
Direct (443) 812-3659
Email barnabyrochelle@mailpost.example
NMLS 3902576
Licensed MD

Name Omar Teldouri
Title Mortgage Originator
Office (800) 416-2795 x32
Direct (571) 326-7045
Email oteldouri@bluebirdlending.example
NMLS 1573064
Licensed MD

```html
<!DOCTYPE html>
<html lang="en">
<head>
<meta charset="utf-8">
<title>Bluebird Business Cards</title>
<link href="https://fonts.googleapis.com/css2?family=Lato:wght@400;700&display=swap" rel="stylesheet">
<style>
  :root {
    --page-bg: #d5d6d8;
    --card-bg: #080808;
    --text-light: #f4f4f4;
    --accent-red: #c8323d;
    --accent-olive: #6e6040;
    --accent-cream: #f3dea2;
    --accent-taupe: #8e8572;
  }
  * { margin: 0; padding: 0; box-sizing: border-box; }
  html, body { width: 1200px; height: 877px; overflow: hidden; }
  body {
    background: var(--page-bg);
    font-family: "Lato", sans-serif;
    color: var(--text-light);
    position: relative;
  }
  .card {
    position: absolute;
    width: 483px;
    height: 275px;
    background: var(--card-bg);
    border-radius: 28px;
    overflow: hidden;
  }
  .card--dorian   { left: 94px;  top: 118px; --accent: var(--accent-red);   --name-top: 54px; --title-top: 77px; --contact-top: 108px; --licence-top: 172px; }
  .card--marlene  { left: 622px; top: 119px; --accent: var(--accent-olive); --name-top: 55px; --title-top: 80px; --contact-top: 119px; --licence-top: 195px; }
  .card--rochelle { left: 69px;  top: 479px; --accent: var(--accent-cream); --name-top: 55px; --title-top: 82px; --contact-top: 110px; --licence-top: 186px; }
  .card--omar     { left: 621px; top: 486px; --accent: var(--accent-taupe); --name-top: 56px; --title-top: 79px; --contact-top: 112px; --licence-top: 183px; }

  .card-name, .card-title, .contact-list, .licence { position: absolute; left: 46px; white-space: nowrap; z-index: 2; }
  .card--rochelle .card-name, .card--rochelle .card-title, .card--rochelle .contact-list, .card--rochelle .licence,
  .card--omar .card-name, .card--omar .card-title, .card--omar .contact-list, .card--omar .licence { left: 49px; }

  .card-name { top: var(--name-top); font-size: 19px; line-height: 22px; font-weight: 700; color: var(--accent); letter-spacing: -0.1px; }
  .card-title { top: var(--title-top); font-size: 13px; line-height: 16px; }
  .contact-list { top: var(--contact-top); list-style: none; }
  .contact-list li { display: flex; align-items: center; height: 20px; font-size: 13px; }
  .contact-icon { width: 15px; height: 12px; margin-right: 7px; fill: var(--accent); flex: none; }
  .licence { top: var(--licence-top); font-size: 13px; line-height: 18px; }

  .portrait { position: absolute; bottom: 0; z-index: 1; }
  .card--dorian .portrait   { left: 230px; top: 32px; width: 245px; background: linear-gradient(180deg, #0a0a0a 0%, #3a2a22 22%, #232a42 55%, #1d2338 100%); border-radius: 90px 90px 0 0; }
  .card--marlene .portrait  { left: 234px; top: 17px; width: 231px; background: linear-gradient(180deg, #0a0a0a 0%, #4a3424 25%, #5b5a3a 60%, #6a6c4a 100%); border-radius: 80px 80px 0 0; }
  .card--rochelle .portrait { left: 285px; top: 12px; width: 159px; background: linear-gradient(180deg, #0a0a0a 0%, #7a5a34 20%, #d9ab8c 55%, #e8c4a8 100%); border-radius: 60px 60px 0 0; }
  .card--omar .portrait     { left: 209px; top: 34px; width: 268px; background: linear-gradient(180deg, #0a0a0a 0%, #3c2b23 22%, #8a8e86 60%, #a3a79e 100%); border-radius: 100px 100px 0 0; }
</style>
</head>
<body>
<svg width="0" height="0" style="position:absolute">
  <defs>
    <symbol id="icon-office" viewBox="0 0 16 13">
      <path d="M1 4.5C1 2 4 1 8 1s7 1 7 3.5v1.3h-3.2V4.2H4.2v1.6H1z"/>
      <path d="M4.8 5.2h6.4l2.6 5.8V12H2.2v-1z"/>
    </symbol>
    <symbol id="icon-direct" viewBox="0 0 16 16">
      <path d="M3.2 1.2l2.4 2.9-1.4 1.8c.9 2.3 2.6 4 4.9 5l1.8-1.4 2.9 2.4-1.6 2.3C6.6 13.7 2.3 9.4 1 3z"/>
      <path d="M9 1.5a5.5 5.5 0 0 1 5.5 5.5h-1.3A4.2 4.2 0 0 0 9 2.8zM9 4a3 3 0 0 1 3 3h-1.3A1.7 1.7 0 0 0 9 5.3z"/>
    </symbol>
    <symbol id="icon-mail" viewBox="0 0 16 12">
      <path d="M0 0h16v1.2L8 6.4 0 1.2z"/>
      <path d="M0 2.8l8 5.2 8-5.2V12H0z"/>
    </symbol>
  </defs>
</svg>

<article class="card card--dorian">
  <h2 class="card-name">Dorian Pelletier</h2>
  <p class="card-title">Mortgage Originator</p>
  <ul class="contact-list">
    <li><svg class="contact-icon"><use href="#icon-office"/></svg>(800) 416-2795 x66</li>
    <li><svg class="contact-icon"><use href="#icon-direct"/></svg>(404) 263-5147</li>
    <li><svg class="contact-icon"><use href="#icon-mail"/></svg>dpelletier@bluebirdlending.example</li>
  </ul>
  <p class="licence">NMLS 3156702<br>Licensed MD</p>
  <div class="portrait" role="img" aria-label="Portrait photo of Dorian Pelletier in a navy suit with red tie"></div>
</article>

<article class="card card--marlene">
  <h2 class="card-name">Marlene Obadofor</h2>
  <p class="card-title">Mortgage Originator</p>
  <ul class="contact-list">
    <li><svg class="contact-icon"><use href="#icon-office"/></svg>(800) 416-2795 x65</li>
    <li><svg class="contact-icon"><use href="#icon-direct"/></svg>(240) 615-2079</li>
    <li><svg class="contact-icon"><use href="#icon-mail"/></svg>mobadofor@bluebirdlending.example</li>
  </ul>
  <p class="licence">NMLS 3817465<br>Licensed MD</p>
  <div class="portrait" role="img" aria-label="Portrait photo of Marlene Obadofor in an olive blazer"></div>
</article>

<article class="card card--rochelle">
  <h2 class="card-name">Rochelle Barnaby</h2>
  <p class="card-title">Mortgage Originator</p>
  <ul class="contact-list">
    <li><svg class="contact-icon"><use href="#icon-office"/></svg>(800) 416-2795 x67</li>
    <li><svg class="contact-icon"><use href="#icon-direct"/></svg>443) 812-3659</li>
    <li><svg class="contact-icon"><use href="#icon-mail"/></svg>barnabyrochelle@mailpost.example</li>
  </ul>
  <p class="licence">NMLS 3902576<br>Licensed MD</p>
  <div class="portrait" role="img" aria-label="Portrait photo of Rochelle Barnaby in a blush satin blouse"></div>
</article>

<article class="card card--omar">
  <h2 class="card-name">Omar Teldouri</h2>
  <p class="card-title">Mortgage Originator</p>
  <ul class="contact-list">
    <li><svg class="contact-icon"><use href="#icon-office"/></svg>(800) 416-2795 x32</li>
    <li><svg class="contact-icon"><use href="#icon-direct"/></svg>(571) 326-7045</li>
    <li><svg class="contact-icon"><use href="#icon-mail"/></svg>oteldouri@bluebirdlending.example</li>
  </ul>
  <p class="licence">NMLS 1573064<br>Licensed MD</p>
  <div class="portrait" role="img" aria-label="Portrait photo of Omar Teldouri in a sage blazer"></div>
</article>
</body>
</html>
```